Bonus/Contractor Pack Sticker

Need a sticker for a current promotion we are running. We are a Building Material company which needs a sticker to apply to existing packaging. We would like the design to be visible from a distance and to have the colour Red.

The sticker will be 6" wide by 4" tall and shall be split in the middle to be wrapped around the corner of the box. (as shown in the example)

Words which need to be included on the sticker are
"Bonus 100pcs Lifetime Durable Wedges Inside"

Target Market(s)

Contractors?Do-it Yourselfers

Industry/Entity Type

Construction

Colors
ec1f27

Requirements
Must have
• Red

```html
<!DOCTYPE html>
<html lang="en">
<head>
<meta charset="utf-8">
<title>Bonus Wedges Sticker</title>
<link rel="stylesheet" href="https://fonts.googleapis.com/css2?family=Open+Sans:wght@700;800&display=swap">
<style>
  :root {
    --brand-red: #ec1f27;
    --ribbon-red: #d81e25;
    --ribbon-dark: #a9141a;
    --ribbon-light: #f04a4f;
    --ink: #2b2b2b;
    --paper: #ffffff;
    --frame: #555555;
  }
  html, body {
    margin: 0;
    padding: 0;
    width: 1200px;
    height: 879px;
    overflow: hidden;
    background: var(--paper);
  }
  .sticker {
    position: relative;
    width: 1200px;
    height: 879px;
    background: var(--paper);
    font-family: "Open Sans", Arial, sans-serif;
  }
  .sticker-art {
    position: absolute;
    inset: 0;
  }
  .headline {
    position: absolute;
    left: 0;
    width: 1180px;
    top: 162px;
    margin: 0;
    text-align: center;
    font-weight: 800;
    font-size: 204px;
    line-height: 1;
    letter-spacing: -3px;
    color: var(--brand-red);
    text-shadow: -13px 8px 0 var(--ink);
  }
  .offer {
    position: absolute;
    left: 0;
    width: 1170px;
    top: 346px;
    margin: 0;
    text-align: center;
    font-weight: 800;
    font-size: 85px;
    line-height: 89px;
    color: var(--paper);
    -webkit-text-stroke: 12px var(--ink);
    paint-order: stroke fill;
    text-shadow: -3px 4px 0 var(--ink);
  }
  .offer span { display: block; }
</style>
</head>
<body>
<div class="sticker">
  <svg class="sticker-art" width="1200" height="879" viewBox="0 0 1200 879">
    <defs>
      <radialGradient id="bow-fill" cx="0.5" cy="0.45" r="0.55">
        <stop offset="0" stop-color="var(--ribbon-dark)"/>
        <stop offset="0.45" stop-color="var(--ribbon-red)"/>
        <stop offset="1" stop-color="var(--ribbon-light)"/>
      </radialGradient>
      <linearGradient id="wedge-fill" x1="0" y1="0" x2="1" y2="1">
        <stop offset="0" stop-color="var(--brand-red)"/>
        <stop offset="1" stop-color="var(--ribbon-dark)"/>
      </linearGradient>
      <clipPath id="frame-clip">
        <rect x="51" y="107" width="1100" height="732"/>
      </clipPath>
    </defs>
    <g clip-path="url(#frame-clip)">
      <path class="ribbon-band" d="M40 140 C230 150 420 200 580 420 L545 460 C400 270 220 215 40 200 Z" fill="var(--ribbon-red)"/>
      <path class="ribbon-band" d="M640 500 C800 600 980 650 1160 660 L1160 780 C960 760 780 680 600 560 Z" fill="var(--ribbon-red)"/>
      <rect role="img" aria-label="Red gift bow illustration" class="gift-bow" x="286" y="286" width="600" height="447" rx="200" fill="url(#bow-fill)"/>
      <rect role="img" aria-label="Red plastic tile wedges, top right" class="wedge-group" x="895" y="107" width="256" height="236" rx="24" fill="url(#wedge-fill)"/>
      <rect role="img" aria-label="Red plastic tile wedges, bottom left" class="wedge-group" x="57" y="552" width="305" height="287" rx="24" fill="url(#wedge-fill)"/>
    </g>
    <rect class="sticker-frame" x="51" y="107" width="1100" height="732" fill="none" stroke="var(--frame)" stroke-width="2"/>
  </svg>
  <h1 class="headline">Bonus</h1>
  <p class="offer">
    <span>100 pcs</span>
    <span>Lifetime</span>
    <span>Durable Wedges</span>
    <span>Inside</span>
  </p>
</div>
</body>
</html>
```